CASH PAYMENT DISCOUNT NOTICE POSTED IN CASH REGISTER AREA

LOOKING TO MAKE A FLYER OR A POSTED NOTICE FOR CUSTOMERS PAYING FOR OVER-THE-COUNTER MERCHANDISE AND WHO PAY BY CASH METHOD TO GET A 4% CASH DISCOUNT.
PRESCRIPTIONS ARE EXCLUDED FROM THIS CASH DISCOUNT.

Target Market(s)

RETAIL CUSTOMERS

Industry/Entity Type

RETAIL PHARMACY

Colors
0054AA
0677BA
7BADD7
CADEEF
E8F1F8
EB3D1F
EC4F4E
F09395
F8D3D4
FCEDEE

Requirements
Must have
• LOGO COLORS
Nice to have
• EYE CATCHING

```html
<!DOCTYPE html>
<html lang="en">
<head>
<meta charset="utf-8">
<title>Lindale Pharmacy – Cash Discount</title>
<link rel="stylesheet" href="https://fonts.googleapis.com/css2?family=Roboto:wght@300;400;700;900&family=Lora:wght@600&family=Kaushan+Script&display=swap">
<style>
  :root {
    --blue-deep: #0054AA;
    --blue-mid: #0677BA;
    --blue-slate: #4a6690;
    --blue-band: #1f5fa3;
    --red-main: #EB3D1F;
    --red-soft: #EC4F4E;
    --white: #ffffff;
    --photo-light: #f4f2ef;
    --photo-warm: #efe3d6;
    --photo-cool: #dfe8e4;
  }
  * { margin: 0; padding: 0; box-sizing: border-box; }
  html, body { width: 919px; height: 1200px; overflow: hidden; background: var(--white); }
  .flyer {
    position: relative;
    width: 919px;
    height: 1200px;
    overflow: hidden;
    font-family: "Roboto", Arial, sans-serif;
    color: var(--white);
  }
  .flyer-backdrop { position: absolute; inset: 0; }

  .brand {
    position: absolute;
    top: 86px;
    right: 52px;
    display: flex;
    align-items: center;
    gap: 12px;
  }
  .brand-dot {
    width: 22px; height: 22px;
    border-radius: 50%;
    background: var(--red-main);
  }
  .brand-name {
    font-family: "Roboto", Arial, sans-serif;
    font-weight: 700;
    font-size: 30px;
    color: var(--blue-deep);
    letter-spacing: 0.5px;
  }

  .pill {
    position: absolute;
    left: 0;
    width: 231px;
    height: 66px;
    border-radius: 0 33px 33px 0;
    background: linear-gradient(90deg, var(--blue-mid), var(--blue-deep));
    display: flex;
    align-items: center;
    justify-content: center;
    text-align: center;
    font-family: "Lora", Georgia, serif;
    font-weight: 600;
    color: var(--white);
    letter-spacing: 2px;
  }
  .pill-merchandise { top: 165px; font-size: 21px; }
  .pill-payment { top: 257px; font-size: 19px; line-height: 1.2; }

  .discount-badge {
    position: absolute;
    left: 0;
    top: 348px;
    width: 246px;
    height: 246px;
    border-radius: 0 50% 50% 50%;
    border-top-left-radius: 0;
    background: linear-gradient(90deg, var(--red-soft), var(--red-main));
    clip-path: circle(123px at 123px 123px);
  }
  .discount-label {
    position: absolute;
    left: 22px;
    top: 40px;
    font-weight: 700;
    font-size: 18px;
    letter-spacing: 3.5px;
    line-height: 25px;
  }
  .discount-value {
    position: absolute;
    left: 0;
    width: 232px;
    top: 90px;
    text-align: center;
    font-weight: 900;
    font-size: 96px;
    line-height: 1;
  }

  .tagline {
    position: absolute;
    left: 46px;
    top: 872px;
    font-family: "Kaushan Script", cursive;
    font-size: 34px;
    line-height: 44px;
  }
  .tagline span { display: block; }
  .tagline span + span { padding-left: 52px; }

  .contact {
    position: absolute;
    top: 1004px;
    font-weight: 300;
    font-size: 16px;
    line-height: 21px;
  }
  .contact-address { left: 82px; }
  .contact-lines { left: 554px; }
  .contact-row { display: flex; }
  .contact-key { width: 68px; }
  .contact-email { font-weight: 700; }

  .hours {
    position: absolute;
    left: 0; right: 0;
    top: 1068px;
    text-align: center;
    font-weight: 300;
    font-size: 16px;
    line-height: 22px;
  }
  .website {
    position: absolute;
    left: 0; right: 0;
    top: 1144px;
    text-align: center;
    font-weight: 700;
    font-size: 17px;
  }
</style>
</head>
<body>
<main class="flyer">
  <svg class="flyer-backdrop" width="919" height="1200" viewBox="0 0 919 1200" aria-hidden="false">
    <defs>
      <linearGradient id="redField" x1="0" y1="0" x2="1" y2="0">
        <stop offset="0" stop-color="#EC4F4E"/>
        <stop offset="1" stop-color="#EB3D1F"/>
      </linearGradient>
      <linearGradient id="blueBand" x1="0" y1="0" x2="1" y2="0">
        <stop offset="0" stop-color="#4a6690"/>
        <stop offset="1" stop-color="#1f5fa3"/>
      </linearGradient>
      <linearGradient id="photoTone" x1="0" y1="0" x2="1" y2="1">
        <stop offset="0" stop-color="#efe3d6"/>
        <stop offset="0.45" stop-color="#f4f2ef"/>
        <stop offset="1" stop-color="#dfe8e4"/>
      </linearGradient>
    </defs>
    <rect class="red-field" x="0" y="560" width="919" height="640" fill="url(#redField)"/>
    <path class="blue-band" d="M0,560 L919,440 L919,810 C780,880 620,905 492,903 C330,900 180,820 82,711 L0,640 Z" fill="url(#blueBand)"/>
    <path class="white-swoosh" d="M0,0 H919 V514 C760,760 600,845 465,845 C290,845 120,760 0,618 Z" fill="#ffffff"/>
    <path class="photo-area" role="img" aria-label="Photo of assorted white tablets and green capsules with a glass thermometer" d="M0,0 H919 V230 C860,420 620,640 300,694 C180,700 60,660 0,618 Z" fill="url(#photoTone)"/>
  </svg>

  <div class="brand">
    <span class="brand-dot"></span>
    <span class="brand-name">Lindale Pharmacy</span>
  </div>

  <div class="pill pill-merchandise">Merchandise</div>
  <div class="pill pill-payment">Cash<br>Method Payment</div>

  <div class="discount-badge">
    <div class="discount-label">GET<br>CASH DISCOUNT</div>
    <div class="discount-value">4%</div>
  </div>

  <p class="tagline"><span>You Ring...</span><span>We Bring</span></p>

  <address class="contact contact-address" style="font-style:normal">
    48 Harlow Street<br>Easton, New York 10990
  </address>
  <div class="contact contact-lines">
    <div class="contact-row"><span class="contact-key">Phone</span><span>: 555-014-2736</span></div>
    <div class="contact-row"><span class="contact-key">Email</span><span>: <span class="contact-email">hello@lindalepharmacy.com</span></span></div>
  </div>

  <p class="hours">
    Mon-Thur : 10am-10pm | Fri : 10am-30 Minutes Before Shabbos<br>
    Sat : Motzei Shabbos - Midnight | Sunday Hours : 10am - 10pm
  </p>

  <p class="website">www.lindalepharmacy.com</p>
</main>
</body>
</html>
```